Maple Lantern Business Card

Design of business cards

Target Market(s)

We are aiming as small business owners who need anything from basic business structures, website plans, business processes and quality assurance.

Industry/Entity Type

Business

Colors

Designer to choose colors to be used in the design.

Requirements
Nice to have
• I would prefer one side of the card to use the green from the logo. Prefer to have the same font as the logo.

```html
<!DOCTYPE html>
<html lang="en">
<head>
<meta charset="utf-8">
<title>Maple Lantern Consulting – Business Card</title>
<link rel="stylesheet" href="https://fonts.googleapis.com/css2?family=Cinzel:wght@500&family=Source+Sans+3:wght@400&display=swap">
<style>
  :root {
    --page-bg: #c5cbca;
    --card-dark-1: #0a0a0a;
    --card-dark-2: #1c1d1d;
    --card-light-1: #ffffff;
    --card-light-2: #e9ecec;
    --brand-green: #9fe01c;
    --contact-grey: #868c8c;
    --tile-pale: #c9cdcd;
    --tile-mid: #555a5a;
    --tile-dark: #2a2c2c;
    --tile-soft: #7b8181;
  }
  html, body {
    margin: 0;
    padding: 0;
    overflow: hidden;
  }
  body {
    width: 848px;
    height: 1200px;
    background: var(--page-bg);
    position: relative;
  }
  .card {
    position: absolute;
    left: 104px;
    width: 638px;
    height: 337px;
    overflow: hidden;
  }
  .card-front { top: 249px; }
  .card-back { top: 663px; }
  .card-texture {
    position: absolute;
    inset: 0;
  }
  .card-front .card-texture {
    background: radial-gradient(ellipse at 50% 40%, var(--card-dark-2), var(--card-dark-1) 75%);
  }
  .card-back .card-texture {
    background: linear-gradient(135deg, var(--card-light-1), var(--card-light-2) 50%, var(--card-light-1));
  }
  .brand-mark {
    position: absolute;
    left: 196px;
    top: 118px;
    width: 96px;
    height: 96px;
    background: var(--brand-green);
  }
  .brand-name {
    position: absolute;
    left: 312px;
    top: 112px;
    margin: 0;
    font-family: "Cinzel", serif;
    font-weight: 500;
    font-size: 27px;
    line-height: 36px;
    color: var(--brand-green);
  }
  .brand-name span { display: block; }
  .contact-icons {
    position: absolute;
    left: 0;
    top: 0;
  }
  .contact-list {
    position: absolute;
    margin: 0;
    padding: 0;
    list-style: none;
    font-family: "Source Sans 3", sans-serif;
    font-size: 20px;
    color: var(--contact-grey);
  }
  .contact-list li {
    position: absolute;
    white-space: nowrap;
    line-height: 24px;
  }
  .contact-phone { left: 274px; top: 156px; }
  .contact-page { left: 252px; top: 181px; }
  .contact-work { left: 294px; top: 207px; }
  .contact-chirp { left: 252px; top: 232px; }
</style>
</head>
<body>
  <section class="card card-front">
    <div class="card-texture" role="img" aria-label="Dark faceted triangle pattern background"></div>
    <div class="brand-mark"></div>
    <h1 class="brand-name"><span>Maple</span><span>Lantern</span><span>Consulting</span></h1>
  </section>

  <section class="card card-back">
    <div class="card-texture" role="img" aria-label="Light faceted diagonal pattern background"></div>
    <svg class="contact-icons" width="638" height="337" viewBox="0 0 638 337" aria-hidden="true">
      <polygon class="tile-phone" points="181,92 217,128 181,164 145,128" fill="var(--tile-pale)"/>
      <polygon class="tile-page" points="141,128 177,164 141,200 105,164" fill="var(--tile-mid)"/>
      <polygon class="tile-work" points="188,163 224,199 188,235 152,199" fill="var(--tile-dark)"/>
      <polygon class="tile-chirp" points="141,199 177,235 141,271 105,235" fill="var(--tile-soft)"/>
      <path class="icon-phone" d="M172,114 c2,-2 4,-2 5,0 l3,4 c1,2 0,3 -1,4 l-2,1 c1,3 4,7 7,9 l2,-2 c1,-1 3,-1 4,0 l4,3 c2,1 1,3 0,5 l-2,2 c-3,2 -10,-1 -15,-7 c-6,-6 -8,-13 -6,-16 z" fill="#ffffff"/>
    </svg>
    <ul class="contact-list">
      <li class="contact-phone">1-123-456-7890</li>
      <li class="contact-page">pagebook.net/myname</li>
      <li class="contact-work">workline.net/myname</li>
      <li class="contact-chirp">chirper.net/myname</li>
    </ul>
  </section>
</body>
</html>
```